Design a Brazilian children's Bible calendar for 2017

We need someone to design a children's calendar for 2017 with an animal theme.
The format is 21cm x 15cm and we need the front cover and one page with two months as can be seen in the attached files.
Target Market(s)
Brazilian children
Font styles to use
Sans Serif
Requirements
Must have
- Modern, clean design

```html
<!DOCTYPE html>
<html lang="pt-BR">
<head>
<meta charset="utf-8">
<title>Calendário 2017 – Novembro e Dezembro</title>
<link rel="stylesheet" href="https://fonts.googleapis.com/css2?family=Raleway:wght@600;700;800;900&family=Quicksand:wght@400;500&display=swap">
<style>
  :root {
    --sky-top: #c9d2da;
    --mountain: #2d4866;
    --meadow: #4f5a3a;
    --meadow-dark: #2f3626;
    --headline: #e6a825;
    --calendar-green: #86c04f;
    --white: #ffffff;
    --year-red: #a3282a;
    --deer-brown: #9c5a2c;
    --tree-green: #2f5e34;
  }
  * { margin: 0; padding: 0; box-sizing: border-box; }
  html, body { width: 856px; height: 1200px; overflow: hidden; }
  body { background: var(--calendar-green); font-family: "Quicksand", sans-serif; }

  .page { position: relative; width: 856px; height: 1200px; }

  .cover-photo {
    position: absolute; left: 0; top: 0; width: 856px; height: 600px;
    background:
      radial-gradient(ellipse 150px 230px at 600px 360px, #8a5a35 0%, rgba(138,90,53,0.7) 55%, rgba(138,90,53,0) 100%),
      linear-gradient(180deg, var(--sky-top) 0%, #a7b3c0 16%, var(--mountain) 30%, #2a4460 52%, var(--meadow) 74%, var(--meadow-dark) 100%);
  }

  .cover-headline {
    position: absolute; left: 61px; top: 212px;
    font-family: "Raleway", sans-serif; font-weight: 600;
    font-size: 36px; line-height: 37px; color: var(--headline);
  }
  .cover-subline {
    position: absolute; left: 61px; top: 379px;
    font-family: "Raleway", sans-serif; font-weight: 700;
    font-size: 21px; color: var(--headline);
  }

  .calendar { position: absolute; left: 0; top: 600px; width: 856px; height: 600px; background: var(--calendar-green); }

  .art { position: absolute; border-radius: 40px; }
  .art-reindeer {
    left: 68px; top: 38px; width: 272px; height: 184px;
    background: linear-gradient(90deg, var(--tree-green) 0%, var(--deer-brown) 35%, #a8673a 100%);
    opacity: 0.85;
  }
  .art-christmas {
    left: 560px; top: 26px; width: 248px; height: 184px;
    background: linear-gradient(90deg, #e9efe3 0%, var(--tree-green) 40%, #2a5530 70%, #c8383b 100%);
    opacity: 0.85;
  }

  .year {
    position: absolute; left: 345px; top: 142px;
    font-family: "Raleway", sans-serif; font-weight: 900;
    font-size: 62px; line-height: 1; color: var(--year-red); letter-spacing: -1px;
  }

  .month { position: absolute; top: 218px; width: 328px; }
  .month-november { left: 66px; }
  .month-december { left: 462px; }

  .month-name {
    text-align: center; font-family: "Quicksand", sans-serif; font-weight: 400;
    font-size: 52px; line-height: 50px; color: var(--white);
    margin: -13px 0 24px;
  }
  .month-december .month-name { margin-left: -6px; }

  .weekdays, .days {
    display: grid; grid-template-columns: repeat(7, 46.8px);
  }
  .weekday {
    width: 42px; height: 42px; margin: 0 auto; border-radius: 50%;
    background: var(--white); color: var(--year-red);
    font-family: "Raleway", sans-serif; font-weight: 800; font-size: 13px;
    display: flex; align-items: center; justify-content: center;
  }
  .days { margin-top: 16px; grid-auto-rows: 36.4px; }
  .day {
    text-align: center; font-family: "Quicksand", sans-serif; font-weight: 500;
    font-size: 26px; line-height: 36.4px; color: var(--white);
  }
</style>
</head>
<body>
<div class="page">
  <section class="cover-photo" role="img" aria-label="Fotografia de um cervo olhando para trás em um campo de vegetação, com montanhas azuladas e céu nublado ao fundo"></section>
  <h1 class="cover-headline">Lorem ipsum dolor<br>sit amet czonsectetuer<br>adipiscing<br>elit aenean commodo</h1>
  <p class="cover-subline">Lorem ipsum</p>

  <section class="calendar">
    <div class="art art-reindeer" role="img" aria-label="Ilustração de uma rena correndo ao lado de pinheiros, com flocos de neve"></div>
    <div class="art art-christmas" role="img" aria-label="Ilustração de árvore de Natal enfeitada com floco de neve, presentes e bengalas doces"></div>
    <div class="year">2017</div>

    <div class="month month-november">
      <h2 class="month-name">Novembro</h2>
      <div class="weekdays">
        <span class="weekday">DOM</span><span class="weekday">TER</span><span class="weekday">QUA</span><span class="weekday">QUI</span><span class="weekday">QUI</span><span class="weekday">SEX</span><span class="weekday">SÁB</span>
      </div>
      <div class="days">
        <span></span><span></span><span></span>
        <span class="day">1</span><span class="day">2</span><span class="day">3</span><span class="day">4</span>
        <span class="day">5</span><span class="day">6</span><span class="day">7</span><span class="day">8</span><span class="day">9</span><span class="day">10</span><span class="day">11</span>
        <span class="day">12</span><span class="day">13</span><span class="day">14</span><span class="day">15</span><span class="day">16</span><span class="day">17</span><span class="day">18</span>
        <span class="day">19</span><span class="day">20</span><span class="day">21</span><span class="day">22</span><span class="day">23</span><span class="day">24</span><span class="day">25</span>
        <span class="day">26</span><span class="day">27</span><span class="day">28</span><span class="day">29</span><span class="day">30</span>
      </div>
    </div>

    <div class="month month-december">
      <h2 class="month-name">Dezembro</h2>
      <div class="weekdays">
        <span class="weekday">DOM</span><span class="weekday">TER</span><span class="weekday">QUA</span><span class="weekday">QUI</span><span class="weekday">QUI</span><span class="weekday">SEX</span><span class="weekday">SÁB</span>
      </div>
      <div class="days">
        <span></span><span></span><span></span><span></span><span></span>
        <span class="day">1</span><span class="day">2</span>
        <span class="day">3</span><span class="day">4</span><span class="day">5</span><span class="day">6</span><span class="day">7</span><span class="day">8</span><span class="day">9</span>
        <span class="day">10</span><span class="day">11</span><span class="day">12</span><span class="day">13</span><span class="day">14</span><span class="day">15</span><span class="day">16</span>
        <span class="day">17</span><span class="day">18</span><span class="day">19</span><span class="day">20</span><span class="day">21</span><span class="day">22</span><span class="day">23</span>
        <span class="day">24</span><span class="day">25</span><span class="day">26</span><span class="day">27</span><span class="day">28</span><span class="day">29</span><span class="day">30</span>
        <span class="day">31</span>
      </div>
    </div>
  </section>
</div>
</body>
</html>
```